The KEP Groote Eylandt - Menu 2020

I am looking for a new desgin on our menu. Preferbly 1 page but happy for it to be in A3. See attached what we are currently using which was designed by one of our admin people which is ok but is a bit busy. The KEP logo is already in use so this would need to stay as is, otherwise the layout /design /background im happy to review all. This is a beach side pub with simple fresh food.

Target Market(s)

FIFO Workforce as well as young familes residential.

Requirements
Must have
• match the logo.
Nice to have
• on 1 page (not turn over)
Should not have
• Anything not family friendly

```html
<!DOCTYPE html>
<html lang="en">
<head>
<meta charset="utf-8">
<title>The KEP – All Day Bar Menu</title>
<link href="https://fonts.googleapis.com/css2?family=Open+Sans:ital,wght@0,300;0,400;0,600;0,700;0,800;1,300;1,400&display=swap" rel="stylesheet">
<style>
:root{
  --blue:#1aa7e1;
  --ink:#1c1c1c;
  --body:#3a3a3a;
  --sketch:#ececec;
  --paper:#ffffff;
}
*{box-sizing:border-box;margin:0;padding:0}
html,body{width:1200px;height:849px;overflow:hidden;background:var(--paper)}
body{font-family:"Open Sans",sans-serif;color:var(--body);position:relative}
.abs{position:absolute}
.sketch{position:absolute;background:var(--sketch);border-radius:14px;opacity:.8}
.h{font-weight:700;font-size:13.6px;color:var(--ink);letter-spacing:.3px;line-height:21px}
.d{font-weight:300;font-size:12px;line-height:18.2px}
.lines{white-space:nowrap}
.row{display:flex;justify-content:space-between;align-items:baseline}
.price{font-weight:600;font-size:13.4px;color:var(--ink)}
.hrow{display:flex;justify-content:space-between;align-items:baseline}
.add{color:var(--blue);font-weight:300;font-size:12px;line-height:21px}
.note{color:var(--blue);font-style:italic;font-weight:300;font-size:11px;line-height:21px}
.col-left{left:59px;width:236px}
.col-mid-a{left:340px;width:236px}
.col-mid-b{left:622px;width:236px}
.col-right{left:901px;width:237px}
.vrule{position:absolute;width:1px;background:var(--blue)}
.big-v{position:absolute;transform-origin:left top;transform:rotate(-90deg);color:var(--blue);font-weight:800;line-height:.92;white-space:nowrap}
.list .row{font-weight:300;font-size:12px;line-height:23px}
.list .row .price{font-size:13.4px}
.brand-name{font-size:38px;font-weight:800;color:var(--ink);letter-spacing:1px;line-height:1}
</style>
</head>
<body>

<header>
  <div class="abs" style="left:70px;top:40px;font-size:20px;font-weight:800;color:var(--ink);letter-spacing:.4px"><span style="color:var(--blue)">ALL DAY</span> BAR MENU</div>
  <div class="abs" style="left:70px;top:68px;font-size:16px;font-weight:300;color:var(--ink)">Available 11.30am - 8.30pm</div>

  <div class="abs" style="left:480px;top:24px;width:256px;text-align:center">
    <span class="brand-name">THE KEP</span>
  </div>
  <div class="abs" style="left:480px;top:78px;width:256px;text-align:center;font-size:8.6px;font-weight:600;letter-spacing:3px;color:var(--ink)">KESTREL BAY RECREATION CLUB</div>

  <div class="big-v" style="left:925px;top:84px;font-size:38px">ME</div>
  <div class="abs" style="left:1061px;top:21px;transform-origin:left top;transform:rotate(90deg) translateY(-100%);color:var(--blue);font-weight:800;font-size:38px;line-height:.92">NU</div>
  <div class="abs" style="left:965px;top:18px;font-size:23px;font-weight:800;color:var(--ink);line-height:1">LUNCH</div>
  <div class="abs" style="left:965px;top:41px;font-size:11px;font-weight:300;color:var(--ink)">12.00pm - 2.00pm</div>
  <div class="abs" style="left:965px;top:54px;font-size:23px;font-weight:800;color:var(--ink);line-height:1">DINNER</div>
  <div class="abs" style="left:965px;top:75px;font-size:11px;font-weight:300;color:var(--ink)">5.30pm - 8.30pm</div>

  <div class="abs" style="left:0;top:104px;width:1200px;height:1.5px;background:var(--blue)"></div>
  <div class="abs" style="left:0;top:109px;width:1200px;height:1.5px;background:var(--blue)"></div>
</header>

<div class="sketch" role="img" aria-label="Line sketch of chicken wings" style="left:0;top:118px;width:55px;height:216px;border-radius:0 20px 20px 0"></div>
<div class="sketch" role="img" aria-label="Line sketch of garlic bread and vegetables" style="left:0;top:510px;width:55px;height:114px;border-radius:0 20px 0 0"></div>
<div class="sketch" role="img" aria-label="Line sketch of a taco" style="left:1140px;top:210px;width:60px;height:182px;border-radius:40px 0 0 40px"></div>
<div class="sketch" role="img" aria-label="Line sketch of a salad plate" style="left:580px;top:482px;width:293px;height:114px;border-radius:50%"></div>
<div class="sketch" role="img" aria-label="Line sketch of ribs" style="left:322px;top:735px;width:64px;height:100px"></div>
<div class="sketch" role="img" aria-label="Line sketch of a sauce bowl and herbs" style="left:706px;top:632px;width:78px;height:96px;border-radius:40px"></div>
<div class="sketch" role="img" aria-label="Line sketch of a burger and fries" style="left:1100px;top:630px;width:100px;height:219px;border-radius:40px 0 0 0"></div>

<section>
  <div class="abs col-left" style="top:128px">
    <div class="h">CRISPY CHICKEN&nbsp; WINGS</div>
    <div class="d lines" style="margin-top:4px">Your Choice of Sauce (Ranch, Spicy Buffalo,<br>BBQ or South West Sauce)</div>
    <div class="row" style="margin-top:2px"><span class="d" style="font-weight:400">5 Wings</span><span class="price">$7.5</span></div>
    <div class="row" style="margin-top:2px"><span class="d" style="font-weight:400">10 Wings</span><span class="price">$15.0</span></div>
  </div>
  <div class="abs col-left" style="top:258px">
    <div class="hrow"><span class="h">TRIO OF SLIDERS</span><span class="price">$12.0</span></div>
    <div class="d lines" style="margin-top:4px">Smoky Pulled Pork, South West Pulled Beef<br>Brisket and Southern Fried Chicken with<br>Sriarcha Mayo all served with Fresh Slaw</div>
  </div>
  <div class="abs col-left" style="top:357px">
    <div class="hrow"><span class="h">VEGE FRIES</span><span class="price">$8.0</span></div>
    <div class="d lines" style="margin-top:4px">Parsnip, Beets &amp; Carrot Fries with<br>Rosemary Sea Salt and Chipotle Mayo</div>
  </div>
  <div class="abs col-left" style="top:438px">
    <div class="h">CRISPY FRIES</div>
    <div class="row" style="margin-top:3px"><span class="d">Plain Fries</span><span class="price">$6.0</span></div>
    <div class="d" style="margin-top:3px">With Gravy, Shaved Gouda</div>
    <div class="row" style="margin-top:3px"><span class="d">Cheese &amp; Grilled Bacon</span><span class="price">$9.0</span></div>
  </div>
  <div class="abs col-left" style="top:544px">
    <div class="hrow"><span class="h">GARLIC BREAD</span><span class="price">$4.0</span></div>
    <div class="hrow"><span class="h">CHEESY GARLIC BREAD</span><span class="price">$5.0</span></div>
  </div>
</section>

<div class="vrule" style="left:318px;top:136px;height:486px"></div>
<div class="vrule" style="left:878px;top:138px;height:486px"></div>

<section>
  <div class="abs" style="left:524px;top:128px;width:166px">
    <div class="h" style="font-size:14px">BURGERS AND SALADS</div>
    <div class="d" style="font-size:10.8px;line-height:15px">All burgers served with steak chip</div>
    <div style="height:1.5px;background:var(--blue);margin-top:8px"></div>
  </div>

  <div class="abs col-mid-a" style="top:175px">
    <div class="h">PULLED PORK BURGER</div>
    <div class="d" style="margin-top:4px">Pulled Pork, Fresh Slaw, Pickles, &amp; Spicy</div>
    <div class="row"><span class="d">BBQ Sauce On A Brioche Bun</span><span class="price">$22.0</span></div>
  </div>
  <div class="abs col-mid-a" style="top:257px">
    <div class="h">BEEF, BACON &amp; CHEESE BURGER</div>
    <div class="d lines" style="margin-top:4px">Beef Patty, Maple Bacon, Cheddar Cheese,<br>Tomato, Cos Lettuce, Caramelised Onion &amp;<br>Smoky BBQ Sauce On A Seeded</div>
    <div class="row"><span class="d">Hamburger Bun</span><span class="price">$22.0</span></div>
  </div>
  <div class="abs col-mid-a" style="top:374px">
    <div class="h">SOUTHERN FRIED</div>
    <div class="hrow"><span class="h">CHICKEN BURGER</span><span class="price">$22.0</span></div>
    <div class="note">(*Grilled Chicken Available)</div>
    <div class="d lines">Chicken Breast, Sliced Fjordvale, Baby<br>Spinach &amp; Sriracha Mayo On A Brioche Bun</div>
  </div>
  <div class="abs col-mid-a" style="top:498px">
    <div class="h">SOUTH WEST BRISKET ROLL</div>
    <div class="d lines" style="margin-top:4px">Pulled Smokey BBQ Beef Brisket with South<br>West Sauce &amp; Fresh Slaw on A Crusty</div>
    <div class="row"><span class="d">Sourdough Roll</span><span class="price">$22.0</span></div>
    <div class="note">*Ask for Vegetarian Substitutes &amp;</div>
    <div class="note">All Options Can Be Served Bunless</div>
  </div>

  <div class="abs col-mid-b" style="top:175px">
    <div class="h">CAESAR SALAD</div>
    <div class="d lines" style="margin-top:4px">Cos Lettuce, Crispy Garlic Croutons, Bacon,<br>Shaved Parmesan, Free Range Egg, Caesar</div>
    <div class="row"><span class="d">Dressing &amp; Anchovies</span><span class="price">$18.0</span></div>
    <div class="row"><span class="add">Add Grilled Chicken</span><span class="price">$4.0</span></div>
    <div class="row"><span class="add">Add Grilled Prawns</span><span class="price">$8.0</span></div>
  </div>
  <div class="abs col-mid-b" style="top:317px">
    <div class="h">LEAF EATER SALAD</div>
    <div class="d lines" style="margin-top:4px">Baby Spinach, Mixed Green Leaves,<br>Avocado, Roasted Red Peppers, Buffalo<br>Mozzarella, Baked Tortilla Strips Served</div>
    <div class="row"><span class="d">with A Balsamic Reduction</span><span class="price">$16.0</span></div>
    <div class="row"><span class="add">Add Grilled Chicken</span><span class="price">$4.0</span></div>
    <div class="row"><span class="add">Add Grilled Prawns</span><span class="price">$8</span></div>
  </div>
</section>

<section>
  <div class="abs" style="left:895px;top:133px;width:250px">
    <div class="h" style="font-size:13.8px">TACOS, NACHOS OR QUESADILLAS</div>
  </div>
  <div class="abs" style="left:933px;top:166px;width:164px;height:1.5px;background:var(--blue)"></div>

  <div class="abs col-right" style="top:177px">
    <div class="h">TACOS</div>
    <div class="d lines" style="margin-top:4px">Soft Tortilla with Your Choice of Filling Fresh<br>Slaw, Avocado, Sriracha Cream &amp; Lime</div>
    <div class="row"><span class="d">Wedge</span><span class="price">$16.0</span></div>
  </div>
  <div class="abs col-right" style="top:277px">
    <div class="h">NACHOS</div>
    <div class="d lines" style="margin-top:4px">Toasted Corn Chips Topped with Your<br>Choice of Filling Avocado, Fresh Tomato<br>Salsa, Melted Cheese, Sour Cream &amp;</div>
    <div class="row"><span class="d">Jalapenos</span><span class="price">$18.0</span></div>
  </div>
  <div class="abs col-right" style="top:395px">
    <div class="h">QUESADILLAS</div>
    <div class="d lines" style="margin-top:4px">Toasted Tortilla with Your Choice of Filling<br>Baby Spinach, Roasted Red Pepper, Gouda</div>
    <div class="row"><span class="d">&amp; Buffalo Mozzarella</span><span class="price">$16.0</span></div>
  </div>
  <div class="abs" style="left:898px;top:504px;font-weight:800;font-size:13.6px;color:var(--blue);letter-spacing:.3px">CHOOSE YOUR FILLING BELOW:</div>
  <div class="abs col-right" style="top:538px">
    <div class="d" style="line-height:21px">Smokey BBQ Pulled Pork</div>
    <div class="d" style="line-height:21px">Southern Fried Chicken</div>
    <div class="d" style="line-height:21px">South West Pulled Beef Brisket</div>
    <div class="row"><span class="d" style="line-height:21px">Chilli Black Bean Grilled Cajun Prawns</span><span class="price">$6.0</span></div>
  </div>
</section>

<div class="abs" style="left:0;top:624px;width:1200px;height:1.5px;background:var(--blue)"></div>

<section>
  <div class="big-v" style="left:57px;top:822px;font-size:46px">MAINS</div>
  <div class="abs" style="left:108px;top:652px;font-size:11.4px;font-weight:300;color:var(--blue)">All meals served with 2 sides</div>
  <div class="abs list" style="left:108px;top:667px;width:210px">
    <div class="row"><span>Sticky BBQ Pork Ribs ½ Rack</span><span class="price">$35.0</span></div>
    <div class="row"><span>Battered Fish and Chips</span><span class="price">$24.0</span></div>
    <div class="row"><span>Chicken Schnitzel</span><span class="price">$25.0</span></div>
    <div class="row"><span>Chicken Parmigiana</span><span class="price">$28.0</span></div>
    <div class="row"><span>400g Rib Fillet On The Bone</span><span class="price">$42.0</span></div>
    <div class="row"><span>300g Scotch Fillet</span><span class="price">$35.0</span></div>
    <div class="row"><span>400g Wagyu Rump</span><span class="price">$35.0</span></div>
  </div>
</section>

<section>
  <div class="big-v" style="left:406px;top:828px;font-size:40px">SIDES &amp;<br>SAUCES</div>
  <div class="abs d" style="left:492px;top:646px;width:235px;font-size:11.6px">
    <div><b style="color:var(--blue);font-weight:600">SIDE #1:</b> Creamy Mashed Potato or Seasoned Steak Chips</div>
    <div style="margin-top:3px"><b style="color:var(--blue);font-weight:600">SIDE #2:</b> Green Salad, Fresh Slaw. Seasonal Vegetables or Mini Caesar Salad</div>
  </div>
  <div class="abs d" style="left:492px;top:725px;width:230px;font-size:11.6px">
    <div class="row"><span>Char Grilled Cajun Corn on the Cob</span><span class="price">$5.0</span></div>
    <div style="margin-top:5px">Creamy Mushroom - Peppercorn Sauce - Traditional Gravy - Smoky BBQ Sauce -</div>
    <div class="row"><span>Bearnaise Sauce</span><span class="price">$2.0</span></div>
    <div class="row" style="margin-top:6px"><span>Extra Sauces</span><span class="price">$1.5</span></div>
  </div>
</section>

<section>
  <div class="abs" style="left:804px;top:654px;width:90px;text-align:center;color:var(--ink)">
    <div style="font-size:11.4px;font-weight:600;letter-spacing:-.4px;line-height:14px">All Kids Meals $9</div>
    <div style="font-size:7.2px;font-style:italic;line-height:9px">WITH A LITTLE CUP OF<br>ICE-CREAM &amp; TOPPING</div>
  </div>
  <div class="big-v" style="left:801px;top:828px;font-size:47px">KIDS<br>MENU</div>
  <div class="abs d" style="left:908px;top:661px;width:240px;font-size:12px;font-weight:300;line-height:15px">
    <div style="margin-bottom:10px">Steak with Chips &amp; Veg</div>
    <div style="margin-bottom:10px">Cheeseburger &amp; Fries</div>
    <div style="margin-bottom:10px">Griled Chicken Burger w/ Cheese, Lettuces, Mayo &amp; Fries</div>
    <div style="margin-bottom:10px">Spaghetti Bolognaise</div>
    <div style="margin-bottom:10px">Fish &amp; Chips</div>
    <div>Mini Southern Fried Chicken bites &amp; chips</div>
  </div>
</section>

</body>
</html>
```